Business Cards and Stationery for software company
For Software Company
Use same font as used in my logo
Eurostile-Black, Eurostile Extended #2
Bright & Fun-filled
Dorian Welby
Vice President
40627 NE 73rd Avenue Suite 815
Brennick, WA 98604
dorianw@halvorquotes.com
www.tandrafix.com
Please keep it simple. I'm open to other fonts as long as they work with the Eurostile we currently use. Arial will be the basis for our website. Don't need to include address necessarily

```html
<!DOCTYPE html>
<html lang="en">
<head>
<meta charset="utf-8">
<title>Tandrafix Business Card</title>
<link rel="stylesheet" href="https://fonts.googleapis.com/css2?family=Arimo:wght@400;700&family=Michroma&display=swap">
<style>
  :root {
    --backdrop: #5a2a14;
    --card-fill: rgba(255, 255, 255, 0.10);
    --card-edge: rgba(255, 255, 255, 0.75);
    --text-light: #f4ece6;
    --text-soft: rgba(244, 236, 230, 0.78);
    --brand-red: #e0192f;
  }
  * { margin: 0; padding: 0; box-sizing: border-box; }
  html, body {
    width: 1200px;
    height: 901px;
    overflow: hidden;
    background: var(--backdrop);
  }
  .stage {
    position: relative;
    width: 1200px;
    height: 901px;
    display: flex;
    align-items: center;
    justify-content: center;
    gap: 40px;
  }
  .card {
    position: relative;
    width: 540px;
    height: 309px;
    background: var(--card-fill);
    border: 2px solid var(--card-edge);
    border-radius: 10px;
    font-family: "Arimo", Arial, sans-serif;
    color: var(--text-light);
  }
  /* contact side */
  .contact-list {
    position: absolute;
    top: 40px;
    left: 38px;
    list-style: none;
  }
  .contact-row {
    display: flex;
    font-size: 13px;
    line-height: 22px;
  }
  .contact-label {
    width: 58px;
    color: var(--text-soft);
    font-size: 10px;
    letter-spacing: 1px;
    text-transform: uppercase;
    line-height: 22px;
  }
  .contact-value { white-space: nowrap; }
  .contact-name { font-weight: 700; font-size: 15px; }
  .web-block {
    position: absolute;
    left: 38px;
    top: 200px;
    font-size: 13px;
    line-height: 20px;
  }
  .web-label { color: var(--text-soft); }
  .brand-mark {
    display: flex;
    align-items: center;
    gap: 10px;
    color: var(--brand-red);
    font-family: "Arimo", Arial, sans-serif;
    font-weight: 700;
    letter-spacing: 2px;
  }
  .brand-square {
    width: 14px;
    height: 14px;
    background: var(--brand-red);
  }
  .brand-mark--corner {
    position: absolute;
    right: 34px;
    bottom: 30px;
    font-size: 22px;
  }
  /* logo side */
  .card--front {
    display: flex;
    align-items: center;
    justify-content: center;
  }
  .brand-mark--hero { font-size: 46px; }
  .brand-mark--hero .brand-square { width: 30px; height: 30px; }
</style>
</head>
<body>
  <main class="stage">
    <section class="card card--back" aria-label="Contact side">
      <ul class="contact-list">
        <li class="contact-row"><span class="contact-label">Name</span><span class="contact-value contact-name">Dorian Welby</span></li>
        <li class="contact-row"><span class="contact-label">Title</span><span class="contact-value">Vice President</span></li>
        <li class="contact-row"><span class="contact-label">Addr</span><span class="contact-value">40627 NE 73rd Avenue Suite 815<br>Brennick, WA 98604</span></li>
        <li class="contact-row"><span class="contact-label">Tel</span><span class="contact-value">360-555-0148</span></li>
        <li class="contact-row"><span class="contact-label">Mail</span><span class="contact-value">dorianw@halvorquotes.com</span></li>
      </ul>
      <div class="web-block">
        <div class="web-label">Web address</div>
        <div class="web-url">www.tandrafix.com</div>
      </div>
      <div class="brand-mark brand-mark--corner"><span class="brand-square"></span>TANDRAFIX</div>
    </section>

    <section class="card card--front" aria-label="Logo side">
      <div class="brand-mark brand-mark--hero"><span class="brand-square"></span>TANDRAFIX</div>
    </section>
  </main>
</body>
</html>
```